Ondas Tierra - Stationery and Presentation Materials
Biz card, letterhead, envelope, presentation folder
Bright & Fun-filled
Martin Coble
E.S.
Tel. +503.2417.8836
Cel. +503.7396.1052
U.S. +1.800.555.0147 x3061
U.S.
ondastierra.led@correoplano.com
PLEASE, DON'T POST EMAIL IN DRAFTS.
--The business is rental of large LED screens for visuals, which are made of thousands of tiny lights.
---Please give a range of crazy/abstract as well as aggressive but traditional/corporate concepts for all items in subtitle.
---The presentation folder is to digitally insert fotos later for printing. Borders are key. A CD will be included, on a plastic peg anywhere in the folder, and CD design must blend with folder graphics on the point where CD sits.
Minimal.
---try wrap-around logo
----1 "wild concept" if anyone is willing - background is very tiny, SHINING, white lights (almost pixel-looking), with the logo symbol on top.

```html
<!DOCTYPE html>
<html lang="es">
<head>
<meta charset="utf-8">
<title>Ondas Tierra – Papelería</title>
<link href="https://fonts.googleapis.com/css2?family=Montserrat:wght@700&family=Open+Sans:wght@400;600&display=swap" rel="stylesheet">
<style>
  :root{
    --backdrop:#ece8e2;
    --paper:#ffffff;
    --red:#e0262b;
    --orange:#f39a1c;
    --amber:#f7b52a;
    --violet:#4b2a8c;
    --blue:#2f6fc6;
    --ink:#3b3f8f;
    --text:#555a66;
    --shadow:0 3px 10px rgba(0,0,0,.22);
  }
  *{box-sizing:border-box;margin:0;padding:0}
  html,body{width:1200px;height:761px;overflow:hidden;background:var(--backdrop)}
  .stage{position:relative;width:1200px;height:761px;font-family:"Open Sans",sans-serif}
  .sheet{position:absolute;background:var(--paper);box-shadow:var(--shadow);overflow:hidden}
  .sheet svg{position:absolute;left:0;top:0}
  .brand{position:absolute;display:flex;align-items:center;gap:8px;
    font-family:"Montserrat",sans-serif;font-weight:700;color:var(--ink);white-space:nowrap}
  .brand .mark{display:block;background:var(--red)}
  .brand.light{color:#fff}
  .brand.light .mark{background:#fff}

  .folder{left:72px;top:48px;width:384px;height:528px}
  .folder .brand{left:40px;top:44px;font-size:30px}
  .folder .brand .mark{width:26px;height:26px}

  .letterhead{left:444px;top:48px;width:468px;height:636px}
  .letterhead .brand{left:22px;top:20px;font-size:26px}
  .letterhead .brand .mark{width:22px;height:22px}
  .letterhead .contact{position:absolute;right:26px;top:560px;color:#fff;font-size:8px;line-height:12px;text-align:left}

  .envelope{left:168px;top:396px;width:564px;height:240px}
  .envelope .brand{left:28px;top:34px;font-size:26px}
  .envelope .brand .mark{width:22px;height:22px}
  .envelope .contact{position:absolute;left:390px;top:84px;color:var(--text);font-size:8px;line-height:12px}

  .card{position:absolute;left:936px;width:204px;height:120px;box-shadow:var(--shadow);overflow:hidden;background:var(--paper)}
  .card svg{position:absolute;left:0;top:0}
  .card .brand{font-size:21px}
  .card .brand .mark{width:18px;height:18px}
  .card-name{top:108px}
  .card-name .brand{left:14px;top:12px;font-size:17px}
  .card-name .brand .mark{width:14px;height:14px}
  .card-name .person{position:absolute;right:16px;top:36px;text-align:right;font-size:8px;color:var(--text);line-height:11px}
  .card-name .person strong{display:block;color:var(--red);font-weight:600;font-size:9px}
  .card-logo{top:252px}
  .card-warm{top:396px;background:linear-gradient(100deg,var(--red),var(--orange))}
  .card-cool{top:540px;background:linear-gradient(100deg,var(--blue),var(--violet))}
  .card-logo .brand,.card-warm .brand,.card-cool .brand{left:50%;top:50%;transform:translate(-50%,-50%)}
</style>
</head>
<body>
<main class="stage">

  <section class="sheet folder" aria-label="Carpeta de presentación">
    <svg width="384" height="528" viewBox="0 0 384 528" aria-hidden="true">
      <defs>
        <linearGradient id="warm" x1="0" x2="1"><stop offset="0" stop-color="#e0262b"/><stop offset=".55" stop-color="#f39a1c"/><stop offset="1" stop-color="#f7b52a"/></linearGradient>
        <linearGradient id="cool" x1="0" x2="1"><stop offset="0" stop-color="#4b2a8c"/><stop offset="1" stop-color="#2f6fc6"/></linearGradient>
      </defs>
      <path d="M0 20 L150 -10 M384 20 L230 -10" stroke="#e3e3e3" stroke-width="1.5" fill="none"/>
      <path d="M0 160 C110 140 260 150 384 170 L384 250 C260 232 110 226 0 260 Z" fill="url(#warm)"/>
      <path d="M0 272 C110 252 260 262 384 282 L384 372 C260 354 110 350 0 386 Z" fill="url(#cool)"/>
      <rect x="226" y="170" width="70" height="70" rx="10" fill="#fff" opacity=".85"/>
      <rect x="226" y="290" width="70" height="70" rx="10" fill="#fff" opacity=".85"/>
    </svg>
    <div class="brand"><span class="mark"></span>Ondas Tierra</div>
  </section>

  <section class="sheet letterhead" aria-label="Hoja membretada">
    <svg width="468" height="636" viewBox="0 0 468 636" aria-hidden="true">
      <defs>
        <linearGradient id="warm2" x1="0" x2="1"><stop offset="0" stop-color="#e0262b"/><stop offset=".6" stop-color="#f39a1c"/><stop offset="1" stop-color="#f7b52a"/></linearGradient>
      </defs>
      <rect x="180" y="220" width="110" height="110" rx="14" fill="#f39a1c" opacity=".12"/>
      <path d="M0 540 C120 500 300 520 468 500 L468 636 L0 636 Z" fill="#4b2a8c"/>
      <path d="M0 552 C120 514 300 530 468 512 L468 636 L0 636 Z" fill="url(#warm2)"/>
    </svg>
    <div class="brand"><span class="mark"></span>Ondas Tierra</div>
    <div class="contact">E.S.<br>Tel. +503.2417.8836<br>Cel. +503.7396.1052<br>U.S. +1.800.555.0147 x3061</div>
  </section>

  <section class="sheet envelope" aria-label="Sobre">
    <svg width="564" height="240" viewBox="0 0 564 240" aria-hidden="true">
      <defs>
        <linearGradient id="warm3" x1="0" x2="1"><stop offset="0" stop-color="#e0262b"/><stop offset=".6" stop-color="#f39a1c"/><stop offset="1" stop-color="#e0262b"/></linearGradient>
      </defs>
      <path d="M0 180 C150 160 360 190 564 150 L564 240 L0 240 Z" fill="#4b2a8c"/>
      <path d="M0 190 C150 170 360 200 564 160 L564 240 L0 240 Z" fill="url(#warm3)"/>
    </svg>
    <div class="brand"><span class="mark"></span>Ondas Tierra</div>
    <div class="contact">E.S.<br>Tel. +503.2417.8836<br>Cel. +503.7396.1052<br>U.S. +1.800.555.0147 x3061</div>
  </section>

  <article class="card card-name" aria-label="Tarjeta de presentación, frente">
    <svg width="204" height="120" viewBox="0 0 204 120" aria-hidden="true">
      <path d="M0 96 C60 84 140 100 204 84 L204 120 L0 120 Z" fill="#4b2a8c"/>
      <path d="M0 102 C60 90 140 106 204 90 L204 120 L0 120 Z" fill="#e0262b"/>
    </svg>
    <div class="brand"><span class="mark"></span>Ondas Tierra</div>
    <div class="person"><strong>Martin Coble</strong>E.S. Tel. +503.2417.8836</div>
  </article>

  <article class="card card-logo" aria-label="Tarjeta, reverso blanco">
    <div class="brand"><span class="mark"></span>Ondas Tierra</div>
  </article>

  <article class="card card-warm" aria-label="Tarjeta, reverso cálido">
    <div class="brand light"><span class="mark"></span>Ondas Tierra</div>
  </article>

  <article class="card card-cool" aria-label="Tarjeta, reverso frío">
    <div class="brand light"><span class="mark"></span>Ondas Tierra</div>
  </article>

</main>
</body>
</html>
```